Sales sheet for printing and embroidery apparel items - Copper Fern Prints

I would like a one page flyer or sales sheet that I would use as a template to send different images of apparel we produce. I have attached examples of layouts I like.
- Ideally, it would have space for 3-5 items.
- I would like it one page only - not a folding flyer.
- Our companies name is Copper Fern Prints.
- This will be used for many different products and markets so I don't need wording/copy. You can use wording from the 7Q7 or K81 flyer.

Colors
0054AA
0677BA
7BADD7
CADEEF
E8F1F8
00AB8E
00BBA5
67D7C9
C6EFE9
E9F9F6
FFC000
F8CF3A
FAE287
FDF2CF
FEFAEE

Requirements
Must have
• Places for between 3 and 5 images of apparel (t-shirts, hats etc)

```html
<!DOCTYPE html>
<html lang="en">
<head>
<meta charset="utf-8">
<title>Copper Fern Prints – Sample Merch Kit</title>
<link href="https://fonts.googleapis.com/css2?family=Poppins:wght@400;500;600;700;800&display=swap" rel="stylesheet">
<style>
:root{
  --paper:#ececec;
  --navy:#163d6e;
  --navy-ink:#1b3f73;
  --ink:#111111;
  --yellow:#f8cf3a;
  --gold:#ffc000;
  --orange:#f28a1c;
  --red:#d4231c;
  --white:#ffffff;
  --rule:#c9d4e3;
}
*{margin:0;padding:0;box-sizing:border-box}
html,body{width:984px;height:1200px;overflow:hidden;background:var(--paper)}
body{font-family:'Poppins',sans-serif;color:var(--ink);position:relative}
.sheet{position:absolute;inset:0}
.abs{position:absolute}

/* Header */
.brand-title{left:60px;top:60px;font-size:58px;font-weight:800;color:var(--orange);letter-spacing:-1px;line-height:1}
.kit-title{left:62px;top:126px;font-size:46px;font-weight:700;line-height:1.1}
.kit-rule{left:560px;top:158px;width:360px;height:2px;background:var(--ink)}

.tag{display:flex;height:28px;border-radius:14px;overflow:hidden;font-size:15px;font-weight:700;line-height:28px}
.tag .key{background:var(--orange);padding:0 24px 0 16px;border-radius:14px 0 0 14px}
.tag .val{background:var(--yellow);padding:0 18px;border-radius:14px;margin-left:-12px}
.tag-model{left:60px;top:208px}
.tag-series{left:64px;top:252px}

.warning{left:494px;top:208px}
.warning-head{display:flex;align-items:center;gap:12px;color:var(--red);font-size:36px;font-weight:800;line-height:1}
.warning-text{margin-top:8px;font-size:13.5px;font-weight:700;line-height:1.25;width:440px}

/* Product tiles */
.tile{top:313px;width:195px;height:184px;border-radius:12px}
.tile-1{left:61px;background:radial-gradient(circle at 50% 45%,#6e6a44 0 38%,#b9b08f 70%,#9c9575 100%)}
.tile-2{left:285px;background:radial-gradient(circle at 50% 45%,#111 0 38%,#8c8c8c 72%,#6d6d6d 100%)}
.tile-3{left:509px;background:radial-gradient(circle at 50% 45%,#2232a8 0 38%,#7f8cf0 72%,#7080ea 100%)}
.tile-4{left:733px;background:radial-gradient(circle at 50% 45%,#1a1a1a 0 38%,#8d8d8d 72%,#6e6e6e 100%)}

/* Kit contents */
.contents-title{left:64px;top:534px;font-size:26px;font-weight:800;color:var(--navy-ink);line-height:1}
.item{top:534px;display:flex;align-items:center;gap:14px;font-size:18px;font-weight:500;line-height:1.15}
.num{width:44px;height:44px;border-radius:50%;display:flex;align-items:center;justify-content:center;font-size:22px;font-weight:700;flex:none}
.num-orange{background:var(--orange)}
.num-yellow{background:var(--yellow)}
.num-navy{background:var(--navy);color:var(--white)}
.item-1{left:269px}
.item-2{left:495px}
.item-3{left:718px}
.vsep{top:529px;width:1.5px;height:54px;background:var(--ink)}
.vsep-1{left:471px}.vsep-2{left:703px}

/* Blue section */
.band{left:0;top:609px;width:984px;height:591px;background:var(--navy);color:var(--white)}
.section-title{font-size:24px;font-weight:800;line-height:1}
.order-title{left:60px;top:38px}
.step{top:88px;width:275px;text-align:center}
.step svg{display:block;margin:0 auto 8px;width:48px;height:48px}
.step-head{color:var(--yellow);font-size:20px;font-weight:600;line-height:1.2}
.step-body{font-size:14.5px;line-height:1.3;margin-top:2px}
.step-1{left:55px}.step-2{left:346px}.step-3{left:648px}
.band-vsep{top:86px;width:1.5px;height:172px;background:var(--white)}
.band-vsep-1{left:335px}.band-vsep-2{left:631px}
.band-rule{left:61px;top:280px;width:854px;height:1px;background:var(--rule)}

.about-title{left:62px;top:312px}
.about-text{left:62px;top:342px;width:390px;font-size:15px;line-height:1.25}
.fine-title{left:468px;top:312px;font-size:21px}
.fine-text{left:468px;top:350px;width:460px;font-size:12.5px;line-height:1.3}

.logo{left:61px;top:428px;width:120px;text-align:center}
.logo-mark{width:80px;height:62px;margin:0 auto 8px;background:var(--orange)}
.logo-name{font-size:17px;font-weight:700;line-height:1.1}

.contact-pill{left:224px;top:441px;height:32px;padding:0 22px;border-radius:16px;background:var(--gold);color:var(--navy);font-size:16px;font-weight:800;line-height:32px;letter-spacing:.3px}
.contact-rule{left:470px;top:457px;width:430px;height:1px;background:var(--rule)}
.contact-lead{left:234px;top:484px;font-size:18px;font-weight:400}
.contact-line{left:232px;top:515px;display:flex;gap:18px;font-size:15.5px;font-weight:600;white-space:nowrap}
.contact-line span{display:flex;align-items:center;gap:7px}
.contact-vsep{left:660px;top:488px;width:1.5px;height:56px;background:var(--white)}
.signoff{left:684px;top:488px;font-size:22px;font-weight:800;line-height:1.2;white-space:nowrap}
</style>
</head>
<body>
<main class="sheet">
  <h1 class="abs brand-title">Copper Fern Prints</h1>
  <h2 class="abs kit-title">Sample Merch Kit</h2>
  <div class="abs kit-rule"></div>

  <div class="abs tag tag-model"><span class="key">Model</span><span class="val">CFP Shop T-shirts</span></div>
  <div class="abs tag tag-series"><span class="key">Series</span><span class="val">Summer/Fall 2025 Collection</span></div>

  <div class="abs warning">
    <div class="warning-head">
      <svg width="46" height="40" viewBox="0 0 46 40" aria-hidden="true"><path d="M23 2 L44 38 H2 Z" fill="#d4231c" stroke="#d4231c" stroke-width="3" stroke-linejoin="round"/><rect x="21" y="13" width="4" height="14" rx="2" fill="#fff"/><circle cx="23" cy="32" r="2.4" fill="#fff"/></svg>
      WARNING:
    </div>
    <p class="warning-text">These shirts may cause increased shop morale, envy from competitors, and a high volume of customer demand.</p>
  </div>

  <div class="abs tile tile-1" role="img" aria-label="Olive t-shirt with a custom vehicle print"></div>
  <div class="abs tile tile-2" role="img" aria-label="Black t-shirt with an off-road vehicle print"></div>
  <div class="abs tile tile-3" role="img" aria-label="Royal blue t-shirt with a classic car print"></div>
  <div class="abs tile tile-4" role="img" aria-label="Black hooded sweatshirt with a bold graphic print"></div>

  <div class="abs contents-title">MERCH KIT<br>CONTENTS</div>
  <div class="abs item item-1"><span class="num num-orange">1</span><span>Custom Shop<br>T-shirt</span></div>
  <div class="abs vsep vsep-1"></div>
  <div class="abs item item-2"><span class="num num-yellow">2</span><span>Additional<br>Sample Shirt</span></div>
  <div class="abs vsep vsep-2"></div>
  <div class="abs item item-3"><span class="num num-navy">3</span><span>CFP Ink<br>Pen</span></div>

  <section class="abs band">
    <h3 class="abs section-title order-title">HOW TO START AN ORDER</h3>

    <div class="abs step step-1">
      <svg viewBox="0 0 48 48" aria-hidden="true" fill="none" stroke="#f8cf3a" stroke-width="2.2"><circle cx="28" cy="20" r="14"/><path d="M18 30 L5 43" stroke-linecap="round"/><path d="M20 22 h16 v-4 l-3-4 h-10 l-3 4 z"/><circle cx="23" cy="24" r="2"/><circle cx="33" cy="24" r="2"/></svg>
      <div class="step-head">Choose your ride</div>
      <p class="step-body">Send us a picture, or let us know the make and model of the vehicle you would like featured on your apparel</p>
    </div>
    <div class="abs band-vsep band-vsep-1"></div>
    <div class="abs step step-2">
      <svg viewBox="0 0 48 52" aria-hidden="true" fill="none" stroke="#f8cf3a" stroke-width="2.2" stroke-linejoin="round"><path d="M16 4 L4 10 L8 22 L13 20 V46 H35 V20 L40 22 L44 10 L32 4 C30 9 18 9 16 4 Z"/><path d="M22 40 V26 a2 2 0 0 1 4 0 V34 l6 1 v8 h-9 z"/></svg>
      <div class="step-head">Pick your gear</div>
      <p class="step-body">We will help you choose your t-shirts, sweatshirts or other apparel items and determine sizes and quantities.</p>
    </div>
    <div class="abs band-vsep band-vsep-2"></div>
    <div class="abs step step-3">
      <svg viewBox="0 0 48 48" aria-hidden="true" fill="none" stroke="#f8cf3a" stroke-width="2.2" stroke-linejoin="round" stroke-linecap="round"><path d="M6 42 L30 18"/><path d="M28 10 a8 8 0 0 0 10 10 l4 -4 -6 -1 -1 -6 z"/><path d="M8 6 L14 4 L40 32 L42 42 L32 40 L6 14 Z"/></svg>
      <div class="step-head">We customize</div>
      <p class="step-body">We make the magic happen and our team of expert artists will design your shirts and get a proof out to you. Upon order approval your order will go into production.</p>
    </div>

    <div class="abs band-rule"></div>

    <h3 class="abs section-title about-title">ABOUT US</h3>
    <p class="abs about-text">Copper Fern Prints is a second-generation screen printing company in Millbrook, VA. For over 45 years, we’ve specialized in high-quality custom apparel and merchandise.</p>

    <h3 class="abs section-title fine-title">THE FINE PRINT:</h3>
    <p class="abs fine-text">Please send high-resolution photos of vehicles. When sending additional logos, please send vector images. Note that our shop minimum is 24 pieces for one-color prints and 100 pieces for full-color screen print. We also promise accurate, quality work.</p>

    <div class="abs logo">
      <div class="logo-mark"></div>
      <div class="logo-name">Copper Fern Prints</div>
    </div>

    <div class="abs contact-pill">CONTACT CFP SALES</div>
    <div class="abs contact-rule"></div>
    <p class="abs contact-lead">For more information, email us at</p>
    <div class="abs contact-line">
      <span><svg width="16" height="12" viewBox="0 0 18 13" aria-hidden="true"><rect x="1" y="1" width="16" height="11" fill="none" stroke="#f8cf3a" stroke-width="1.8"/><path d="M1 1 L9 7 L17 1" fill="none" stroke="#f8cf3a" stroke-width="1.8"/></svg>hello@copperferntees.com</span>
      <span><svg width="14" height="14" viewBox="0 0 16 16" aria-hidden="true"><path d="M3 1 L6 1 L7 5 L5 6.5 C6 9 7 10 9.5 11 L11 9 L15 10 L15 13 C15 14 14 15 13 15 C6 15 1 10 1 3 C1 2 2 1 3 1 Z" fill="#f8cf3a"/></svg>555-014-2288</span>
    </div>
    <div class="abs contact-vsep"></div>
    <p class="abs signoff">We look forward to<br>working with you!</p>
  </section>
</main>
</body>
</html>
```